B2B flyer solution for charging infrastructures (One-Pager Din A4, double-sided)

We need a professional design for our flyer in format Din A4/both sides.
Attached you will find the content for the flyer, but we are looking for a modern, professional design.

Some background/context information:
- the product is about a solution for charging and billing of charging infrastructures (for electric cars) in companies
- target group: companies, esp. facility managers, fleet managers, controlling, CTO, CEO
- should be printed and available online
- our website (and most of our current design work): https://vornix-tech.de

In the files you will find:
- photos of reference implementations of our solution (should be included in the flyer)
- stock photos (we are using the one you will find in the current flyer on our presentations, maybe you can use it too to keep some corporate identity.
- our logo
- the current flyer as PDF and as PowerPoint
- a sample presentation we also need for customer communication

It would be nice if the design will align with the existing design work, but bring fresh aspects and will be up-to-date and professional.

Target Market(s)

B2B, companies, fleet managers, facility managers, CTO, CIO

Industry/Entity Type

Enterprises, Charging Solutions for Electric Vehicles

Requirements
Nice to have
• Bright, light design, clean, readable

```html
<!DOCTYPE html>
<html lang="de">
<head>
<meta charset="utf-8">
<title>vornix Professional – Flyer</title>
<link rel="stylesheet" href="https://fonts.googleapis.com/css2?family=Titillium+Web:ital,wght@0,400;0,600;0,700;1,400&display=swap">
<style>
:root{
  --stage:#b9b9b9;
  --ink-dark:#1d1c21;
  --header-dark:#1e2438;
  --pink:#e0359a;
  --purple:#7a5cb8;
  --white:#ffffff;
  --text-light:#e9e7ee;
  --text-muted:#c9c6d0;
  --footer-ink:#1a1a1a;
}
*{box-sizing:border-box;margin:0;padding:0}
html,body{width:1200px;height:833px;overflow:hidden}
body{background:var(--stage);font-family:"Titillium Web",Arial,sans-serif;position:relative;color:var(--text-light)}
.page{position:absolute;top:60px;width:503px;height:712px;background:var(--ink-dark);overflow:hidden;box-shadow:-6px 6px 10px rgba(0,0,0,.35)}
.page--front{left:70px}
.page--back{left:627px}
.hero{position:absolute;left:0;top:0;width:100%;height:189px}
.page--front .hero{background:radial-gradient(ellipse at 75% 55%,#5e6a9a 0%,#2d3556 40%,var(--header-dark) 75%)}
.page--back .hero{background:radial-gradient(ellipse at 78% 50%,#cfe2f5 0%,#7fa6d4 30%,#3c5a8c 60%,var(--header-dark) 90%)}
.brand{position:absolute;left:26px;top:62px;display:flex;align-items:center;gap:8px;font-size:21px;font-weight:600;color:var(--white)}
.brand__dot{width:12px;height:12px;border-radius:50%;background:var(--pink)}
.title-band{position:absolute;left:0;top:99px;width:72%;height:65px;background:linear-gradient(90deg,rgba(255,255,255,.95) 0%,rgba(255,255,255,.85) 70%,rgba(255,255,255,0) 100%);padding:14px 0 0 27px;color:#1b1b1b}
.title-band h1{font-size:27px;line-height:1;font-weight:700}
.title-band p{font-size:13px;font-weight:600;margin-top:4px}
.tagline{position:absolute;left:0;top:189px;width:100%;height:30px;background:linear-gradient(90deg,var(--pink),var(--purple));color:var(--white);font-size:11.5px;text-align:center;line-height:30px}
.intro{position:absolute;left:26px;top:230px;width:460px}
.intro h1{font-size:27px;font-weight:700;line-height:1.05;color:var(--white)}
.intro .sub{font-size:13.4px;margin-top:3px}
.intro .lead{font-size:13.4px;line-height:1.4;margin-top:12px}
.intro .claim{font-size:13.4px;font-style:italic;color:var(--pink);margin-top:1px}
.services{position:absolute;left:26px;top:374px;width:225px}
.services h2{font-size:14px;font-weight:700;color:var(--white);margin-bottom:6px}
ul.bullets{list-style:none}
ul.bullets li{position:relative;padding-left:6px;font-size:9px;line-height:1.35;margin-bottom:5px}
ul.bullets li::before{content:"•";position:absolute;left:0}
.photo{position:absolute;border:1.5px solid #d9d9e0}
.photo--stations{left:263px;top:366px;width:215px;height:167px;border-radius:40px 0 40px 0;background:linear-gradient(180deg,#c99a4e 0%,#8a9a6a 45%,#6b6f6c 70%,#8c8a84 100%)}
.photo--car{left:294px;top:517px;width:191px;height:137px;border-radius:30px 0 30px 0;background:radial-gradient(ellipse at 55% 60%,#3a3a3e 0%,#5b5d62 50%,#8d8f94 100%)}
.card{position:absolute;top:549px;width:230px;height:112px;border-radius:12px;border:1.5px solid #e6d8f2;background:linear-gradient(120deg,var(--pink),var(--purple));padding:12px 11px;color:var(--white)}
.card--benefits{left:17px}
.card--contact{left:256px}
.card h3{font-size:11px;font-weight:700;margin-bottom:4px}
.card ul.bullets li{font-size:9px;margin-bottom:1px;line-height:1.3}
.card p{font-size:9px;line-height:1.35;color:#f6eaf5}
.footer{position:absolute;left:0;bottom:0;width:100%;height:41px;background:var(--white);display:flex;align-items:center;justify-content:space-between;padding:0 17px 0 17px;color:var(--footer-ink);font-size:11px;font-weight:700}
.footer span{display:flex;align-items:center;gap:6px}
.footer svg{width:13px;height:13px}
.audience-head{position:absolute;top:226px;width:100%;text-align:center;font-size:12px}
.audience{position:absolute;top:248px;left:30px;width:445px;display:flex;justify-content:space-between}
.audience__item{width:110px;text-align:center;font-size:11.5px;font-weight:700;line-height:1.3;color:var(--white)}
.audience__item svg{width:22px;height:18px;display:block;margin:0 auto 6px}
.feature{position:absolute}
.feature h2{font-size:12.5px;font-weight:700;color:var(--pink);line-height:1.2;margin-bottom:10px}
.feature p{font-size:9px;line-height:1.35;color:var(--text-muted);margin-bottom:8px}
.feature ul.bullets li{font-weight:600;margin-bottom:3px;color:var(--white)}
.feature--service{left:17px;top:326px;width:215px}
.feature--owner{left:265px;top:326px;width:222px}
.feature--integration{left:17px;top:505px;width:272px}
.divider{position:absolute;left:242px;top:328px;width:1px;height:165px;background:#b9b6c2}
</style>
</head>
<body>

<section class="page page--front">
  <div class="hero" role="img" aria-label="Foto: Ladestecker steckt in einer Ladesäule, unscharfe Lichter im Hintergrund"></div>
  <div class="brand"><span class="brand__dot"></span>vornix-tech.de</div>
  <div class="tagline">vornix - Die Abrechnungslösung für Lade-Infrastruktur in Unternehmen.</div>

  <div class="intro">
    <h1>vornix Professional</h1>
    <p class="sub">die maßgeschneiderte B2B-Abrechnungslösung für Elektromobilität</p>
    <p class="lead">Lade-Infrastruktur-Abrechnungslösungen für Unternehmen,<br>damit Lade-Infrastruktur Erträge statt Kosten produziert.</p>
    <p class="claim">So wird Lade-Infrastruktur von einer Kostenstelle zu einem Profitcenter</p>
  </div>

  <div class="services">
    <h2>Leistungen:</h2>
    <ul class="bullets">
      <li>Vielseitige Abrechnungsmöglichkeiten für Fuhrpark, Mitarbeiter, Partnerunternehmen, Mieter, Kunden und andere.</li>
      <li>Full-Service-Betreuung (Monitoring, Abrechnung, Benutzerbetreuung)</li>
      <li>Integration in ihre Unternehmensabläufe</li>
      <li>Berücksichtigung von Eigentümer/Mieter Konstellationen</li>
    </ul>
  </div>

  <div class="photo photo--stations" role="img" aria-label="Foto: Reihe von Ladesäulen auf einem Parkplatz bei Abendsonne"></div>

  <div class="card card--benefits">
    <h3>Mit vornix Professional profitieren:</h3>
    <ul class="bullets">
      <li>Effizienter Verwaltung von Lade-Infrastruktur</li>
      <li>Umfassende Full-Service-Betreuung</li>
      <li>Nahtloser Integration in Ihre kaufmännischen Prozesse</li>
      <li>Vielseitigen Abrechnungsmöglichkeiten</li>
    </ul>
  </div>
  <div class="card card--contact">
    <h3>Kontaktieren Sie uns</h3>
    <p>Erfahren Sie mehr über vornix und wie wir Ihre Abrechnungsanforderungen erfüllen können. Kontaktieren Sie uns für eine kostenlose Beratung:</p>
  </div>

  <div class="footer">
    <span><svg viewBox="0 0 24 24" fill="none" stroke="#e0359a" stroke-width="2.2"><path d="M5 3h4l2 5-2.5 1.5a11 11 0 0 0 6 6L16 13l5 2v4a2 2 0 0 1-2 2A16 16 0 0 1 3 5a2 2 0 0 1 2-2z"/></svg>+49 (0) 9876 543 210</span>
    <span><svg viewBox="0 0 24 24"><rect x="2" y="5" width="20" height="14" rx="2" fill="#e0359a"/><path d="M2 6l10 7 10-7" fill="none" stroke="#fff" stroke-width="1.6"/></svg>info@vornix-tech.de</span>
    <span><svg viewBox="0 0 24 24" fill="none" stroke="#e0359a" stroke-width="1.8"><circle cx="12" cy="12" r="10"/><ellipse cx="12" cy="12" rx="4" ry="10"/><path d="M2 12h20M4 7h16M4 17h16"/></svg>www.vornix-tech.de</span>
  </div>
</section>

<section class="page page--back">
  <div class="hero" role="img" aria-label="Foto: weißer Ladestecker mit blau leuchtendem Ladering am Elektroauto"></div>
  <div class="brand"><span class="brand__dot"></span>vornix-tech.de</div>
  <div class="title-band">
    <h1>vornix Professional</h1>
    <p>die Funktionen im Überblick</p>
  </div>
  <div class="tagline">vornix - Die Abrechnungslösung für Lade-Infrastruktur in Unternehmen.</div>

  <p class="audience-head">Verrechnung von Ladevorgängen für</p>
  <div class="audience">
    <div class="audience__item"><svg viewBox="0 0 44 20" fill="none" stroke="#e0359a" stroke-width="2"><path d="M3 14h38v-4l-6-2-5-5H14L9 8 3 10z"/><circle cx="12" cy="15" r="3" fill="#1d1c21"/><circle cx="32" cy="15" r="3" fill="#1d1c21"/></svg>Fuhrpark,<br>Dienstwagen</div>
    <div class="audience__item"><svg viewBox="0 0 24 20" fill="#e0359a"><circle cx="6" cy="5" r="3"/><circle cx="18" cy="5" r="3"/><circle cx="12" cy="8" r="3.4"/><path d="M1 17a5 5 0 0 1 10 0zM13 17a5 5 0 0 1 10 0zM6 20a6 6 0 0 1 12 0z"/></svg>Mitarbeiter<br>Privatfahrzeuge</div>
    <div class="audience__item"><svg viewBox="0 0 24 20" fill="#e0359a"><circle cx="6" cy="5" r="3"/><circle cx="18" cy="5" r="3"/><circle cx="12" cy="8" r="3.4"/><path d="M1 17a5 5 0 0 1 10 0zM13 17a5 5 0 0 1 10 0zM6 20a6 6 0 0 1 12 0z"/></svg>Kunden und<br>Gäste</div>
    <div class="audience__item"><svg viewBox="0 0 24 20" fill="#e0359a"><rect x="3" y="6" width="6" height="14"/><rect x="10" y="1" width="7" height="19"/><rect x="18" y="9" width="5" height="11"/></svg>Vermieter,<br>Eigentümer</div>
  </div>

  <div class="feature feature--service">
    <h2>Full-Service-Betreuung<br>für sorgenfreies Management</h2>
    <p>vornix übernimmt auf Wunsch alle organisatorischen Belange bei der Verwaltung Ihrer Lade-Infrastruktur, einschließlich:</p>
    <ul class="bullets">
      <li>Monitoring</li>
      <li>Support</li>
      <li>User-Onboarding und -Support</li>
      <li>Handling von Zugangskarten</li>
      <li>Integration von firmeninternen Zugangstoken</li>
    </ul>
  </div>
  <div class="divider"></div>
  <div class="feature feature--owner">
    <h2>Besonderer Aspekt: Eigentümer-<br>Mieter Konstellatione</h2>
    <p>Häufige Situation: Der Mieter eines Objektes benötigt Lade-Infrastruktur, der Eigentümer/ Verwalter möchte nicht zusätzlich belastet werden.</p>
    <ul class="bullets">
      <li>Unterschiedliche Betreibermodelle für verschiedene Situationen (Langzeit-Mieter vs. Kurzzeit-Mieter)</li>
      <li>Kauf-, Miet- und Leasing-Optionen</li>
      <li>Kostenneutral für Eigentümer/Verwalter durch geeignete Abrechnungsmodelle</li>
    </ul>
  </div>

  <div class="feature feature--integration">
    <h2>Perfekte Integration in<br>kaufmännische Prozesse</h2>
    <p>vornix fügt sich nahtlos in die kaufmännischen Strukturen moderner Unternehmen ein und bietet:</p>
    <ul class="bullets">
      <li>Erweitertes Reporting</li>
      <li>Aufschlüsselung und Tarifierung nach Nutzergruppe</li>
      <li>Unterstützung unternehmensinterner Abrechnung und Verrechnung und/oder Zahlungseinzug durch vornix</li>
      <li>Schnittstellen zu Buchhaltung und Lohnbuchhaltung</li>
      <li>Bedarfsgerechte Anpassbarkeit</li>
    </ul>
  </div>
  <div class="photo photo--car" role="img" aria-label="Foto: schwarzes Elektro-SUV an einer Wandladestation in einer Tiefgarage"></div>

  <div class="footer">
    <span><svg viewBox="0 0 24 24" fill="none" stroke="#e0359a" stroke-width="2.2"><path d="M5 3h4l2 5-2.5 1.5a11 11 0 0 0 6 6L16 13l5 2v4a2 2 0 0 1-2 2A16 16 0 0 1 3 5a2 2 0 0 1 2-2z"/></svg>+49 (0) 9876 543 210</span>
    <span><svg viewBox="0 0 24 24"><rect x="2" y="5" width="20" height="14" rx="2" fill="#e0359a"/><path d="M2 6l10 7 10-7" fill="none" stroke="#fff" stroke-width="1.6"/></svg>info@vornix-tech.de</span>
    <span><svg viewBox="0 0 24 24" fill="none" stroke="#e0359a" stroke-width="1.8"><circle cx="12" cy="12" r="10"/><ellipse cx="12" cy="12" rx="4" ry="10"/><path d="M2 12h20M4 7h16M4 17h16"/></svg>www.vornix-tech.de</span>
  </div>
</section>

</body>
</html>
```